Bottle labels and logo for small distillery

Marsh Hollow Distillery is a small beginning project of handcrafted distillery producing cider spirit (same as apple wine spirit) and apple vodka from apple wine. There are not many similar small distilleries in the Baltic Sea region and very few of them produce apple brandy, so the concept and the product itself are unique. That is the reason we are not developing any distinctive brand and we are sticking to two elements – company name ‘Marsh Hollow Distillery OÜ’ and product name ‘Orchardveil’. Best branding solution for us would be to have a clear logo instead of words.

In the future it is most likely that the product range will broaden by some type of sweet liqueurs like apple-liqueur and black-currant-liqueur and both will be mixtures of natural juice and apple brandy.

We have tested the product itself and more or less chosen proper bottle and closing. Example of the shape of the bottle:

https://www.vessel-depot-example.co.uk/Containers/Containers/500ml-containers/500ml-clear-container-Brevo.html

Sizes of bottles:
500 ml Height (without cap) 350 mm, external diameter 60 mm;
375 ml Height (without cap) 330 mm, external diameeter 55 mm;

The bottle cap/closing is going to be waxed, and should look something like that:

http://img.picvault-example.com/qT7Rz.jpg

The design has two separate parts: (1) paper bottle label and (2) print on the bottle.

Front side – printed to the bottle, preferably a symbol without text, for better quality of print rather a vector graphics (monochrome or up to 3-single colour picture). We would like to use the symbol also as an enterprise logo if possible (but logo and bottle print can also be different if designer decides so). It should give a hint to apple based distillate (but, we do not want to narrow down creators fantasy so if you have a good idea please don’t hold back). Just to offer a dumb examples:
https://moodloft-example.com/entry/51830962
https://www.snapboard-example.ca/pin/917263540812355019/?lp=true https://www.stockvista-example.com/image-vector/decorative-apple-flora-ornaments-leaf-flower-208473615?src=QXR_kpLwVb8TyR3HxM_42q-2-50
NB! these are just examples of style, contents are more or less random.

Back side – a rectangular shaped label glued to the bottle. Label should not be a square but rather oblong and narrow. The colour of the label shouldn’t be white but rather light yellow, light brown or light creamy. Some examples:

https://www.snapboard-example.co.uk/pin/720954183627104958 https://www.snapboard-example.co.uk/pin/839172046558213940

Label has to contain such information:
1) (Product in large print) Orchardveil
2) (product) apple wine spirit
3) (Neto amount) 50 cl; / 35 cl
4) (Ethanol in large print) 45%; / 55%
5) (Producer) Produced by Marsh Hollow Distillery, Harjumaa 74211, Paldiski, Lõhmuse 9;
6) (raw material and technology) Made in Estonia. Product is made of Estonian apple wine and distilled in reflux still in small batches
7) (distillate) Distillate 85%
8) (batch no) Batch no: (stamp) …
9) (note) produced with utmost pleasure
10) (note) Consume responsibly
11) (signature) distiller: …

We also need the label to be designed in Estonian as follows:
1) Orchardveil
2) Õunaveini destillaat
3) 50 cl; / 35 cl
4) 45% / 55%
5) Toodetud Marsh Hollow Distillery OÜ poolt, Harjumaal 74211, Paldiski, Lõhmuse 9;
6) Toodetud Eestis, eestimaisest õunaveinist ja destilleeritud käsitööna väikeste partiidena
7) Destillaat 85%
8) Partii nr:
9) Toodetud puhtast rõõmust
10) Tarbige vastutustundlikult!
11) Meister:

Design as such can be the same. Since we are planning to bottle the product in 375 ml and 500 ml bottles and dilute it down to 45% and 55%. So, there should be 37,5 cl 45%, 50 cl 45%; 37,5 cl 55%; 50 cl 55%.

We assume that in case of 37,5 cl and 50 cl bottles we can use the same design and just resize the printed image and paper-label a bit.

Since the product is handmade and high quality we would like to stress credibility. Not as important as the first purchase is the second purchase of clients – the label should not be shocking but rather trustworthy. And classy in the very best sense.

We are hoping to have a long term business relationship with possible future designer.

Target Market(s)

Adult male alcohol consumers

Industry/Entity Type

Food Production

Logo Text

Marsh Hollow Distillery

Colors

Designer to choose colors to be used in the design.

```html
<!DOCTYPE html>
<html lang="en">
<head>
<meta charset="utf-8">
<title>Orchardveil bottle labels</title>
<link rel="stylesheet" href="https://fonts.googleapis.com/css2?family=Arimo:wght@400;700&family=Open+Sans:wght@400&family=Gelasio:wght@700&display=swap">
<style>
  :root{
    --page:#ffffff;
    --halo:#fdfbc6;
    --paper:#fffdd8;
    --frame:#9a6a35;
    --wine:#a3272d;
    --deep-red:#9b0d0d;
    --ink:#2b2b2b;
    --mark-top:#f4efe2;
    --mark-bottom:#e8351f;
  }
  html,body{margin:0;padding:0;overflow:hidden;background:var(--page);}
  .canvas{position:relative;width:1200px;height:1042px;overflow:hidden;background:var(--page);
    font-family:"Arimo",Arial,sans-serif;color:var(--ink);}
  .label{position:absolute;background:var(--halo);border-radius:130px;}
  .label-inner{position:absolute;inset:14px;border:6px solid var(--frame);border-radius:112px;background:var(--paper);}
  .front{left:23px;top:46px;width:369px;height:945px;}
  .back-en{left:417px;top:33px;width:373px;height:942px;}
  .back-et{left:812px;top:29px;width:375px;height:938px;}
  .line{position:absolute;left:0;right:0;text-align:center;transform:translateY(-50%);white-space:nowrap;line-height:1.1;}
  .symbol{position:absolute;left:50%;transform:translateX(-50%);
    background:linear-gradient(to bottom,var(--mark-top) 0%,var(--mark-top) 45%,var(--mark-bottom) 55%,var(--mark-bottom) 100%);
    border-radius:14px;}
  .front .symbol{top:71px;width:275px;height:300px;}
  .back-en .symbol,.back-et .symbol{top:46px;width:130px;height:146px;}
  .wordmark{color:var(--wine);font-family:"Arimo",Arial,sans-serif;font-weight:400;}
  .front .wordmark{font-size:50px;}
  .back-en .wordmark,.back-et .wordmark{font-size:43px;}
  .product-title{font-family:"Gelasio",Georgia,serif;font-weight:700;color:var(--deep-red);font-size:70px;}
  .producer-serif{font-family:"Gelasio",Georgia,serif;font-weight:700;font-size:23px;}
  .subtitle{font-family:"Open Sans",Arial,sans-serif;font-size:25px;}
  .volume{font-size:26px;}
  .ethanol-label{font-size:32px;}
  .ethanol{font-size:60px;}
  .small{font-size:19px;}
  .producer-name{font-size:22px;font-weight:700;}
  .address{font-size:15px;}
  .bold-mid{font-size:22px;font-weight:700;}
  .body{font-size:18px;}
  .body-et{font-size:19px;}
  .batch{font-size:21px;}
  .note{font-size:17px;}
  .signature{position:absolute;transform:translateY(-50%);font-size:21px;}
</style>
</head>
<body>
<div class="canvas">

  <section class="label front">
    <div class="label-inner"></div>
    <div class="symbol" role="img" aria-label="Brand symbol artwork with apples"></div>
    <div class="line wordmark" style="top:416px">Orchardveil</div>
    <div class="line product-title" style="top:546px">Apple</div>
    <div class="line product-title" style="top:629px">Wine</div>
    <div class="line product-title" style="top:708px">Spirit</div>
    <div class="line subtitle" style="top:818px;font-size:24px">Produced by:</div>
    <div class="line producer-serif" style="top:856px">Marsh Hollow Distillery</div>
  </section>

  <section class="label back-en">
    <div class="label-inner"></div>
    <div class="symbol" role="img" aria-label="Brand symbol artwork with apples"></div>
    <div class="line wordmark" style="top:228px">Orchardveil</div>
    <div class="line subtitle" style="top:267px">Apple Wine Spirit</div>
    <div class="line volume" style="top:310px">50 cl/35 cl</div>
    <div class="line ethanol-label" style="top:374px">Ethanol :</div>
    <div class="line ethanol" style="top:429px">45%/55%</div>
    <div class="line small" style="top:492px">Produced by:</div>
    <div class="line producer-name" style="top:521px">Marsh Hollow Distillery,</div>
    <div class="line address" style="top:550px">Harjumaa 74211, Paldiski, Lõhmuse 9</div>
    <div class="line bold-mid" style="top:581px">Made in Estonia.</div>
    <div class="line body" style="top:615px">Product is made of</div>
    <div class="line body" style="top:640px">Estonian apple wine and</div>
    <div class="line body" style="top:664px">distilled in reflux still</div>
    <div class="line body" style="top:688px">in small batches</div>
    <div class="line bold-mid" style="top:721px;font-size:21px">Destillate 85%</div>
    <div class="line batch" style="top:774px">Batch no: ...................</div>
    <div class="line note" style="top:805px">Produce with utmost pleasure</div>
    <div class="line note" style="top:829px">Consume responsibly</div>
    <div class="signature" style="left:68px;top:876px">Distiller:</div>
  </section>

  <section class="label back-et">
    <div class="label-inner"></div>
    <div class="symbol" role="img" aria-label="Brand symbol artwork with apples"></div>
    <div class="line wordmark" style="top:228px">Orchardveil</div>
    <div class="line subtitle" style="top:267px">Õunaveini destillaat</div>
    <div class="line volume" style="top:311px">50 cl/35 cl</div>
    <div class="line ethanol-label" style="top:373px">Ethanol :</div>
    <div class="line ethanol" style="top:429px">45%/55%</div>
    <div class="line small" style="top:496px">Toodetud</div>
    <div class="line producer-name" style="top:522px;font-size:20px">Marsh Hollow Distillery OÜ poolt,</div>
    <div class="line address" style="top:552px">Harjumaal 74211, Paldiski, Lõhmuse 9</div>
    <div class="line body-et" style="top:596px">Toodetud Eestis, eestimaisest</div>
    <div class="line body-et" style="top:623px">õunaveinist ja destilleeritud</div>
    <div class="line body-et" style="top:651px">käsitööna väikeste</div>
    <div class="line body-et" style="top:679px">partiidena</div>
    <div class="line bold-mid" style="top:711px;font-size:21px">Destillaat 85%</div>
    <div class="line batch" style="top:769px">Partii nr: ...................</div>
    <div class="line note" style="top:803px">Toodetud puhtast roomust</div>
    <div class="line note" style="top:826px">Tarbige vastututstundlikult!</div>
    <div class="signature" style="left:68px;top:868px">Meister:</div>
  </section>

</div>
</body>
</html>
```